依頼詳細
昨年商品をご購入いただいた方へ、今年の商品のご案内に同封する手書き、絵手紙風の手紙を作成したいです。
商品は日本一大きな柿です。
温もりのある、手書き風、絵手紙風、書道風など、年齢問わず見ていただけるものを希望します。

商品内容: 柿(桜里柿)
参照HP: http://aobakaki-nouen.jp/
(HPからのリンクでFacebookページもあります)

記載項目
内容:
※イラスト又は手書き文字又は両方で、以下の内容を表現していただきたいです。

①昨年はご購入又はご賞味いただきありがとうございます。というニュアンスのお礼
②ホームページが出来たので、ホームページからの注文が便利とというニュアンスの紹介
③桜里柿と青葉農園の紹介
④オリジナルデザインの小分け袋箱を無料でお付けする旨
希望イメージ
• +5 0 +5
• シンプル
複雑
• 単色
カラフル
• 暗い
明るい
• 日常
高級
• 遊び心
厳粛
• 未来的
伝統的
• 女性的
男性的
希望する色
赤系、黄・オレンジ系
納品ファイル
• 高解像度JPG (.jpg)
• イラストレーター形式 (.ai)
• フォトショップ形式 (.psd)
• PNG形式 (.png)
補足説明
依頼公開後の追記内容
手紙サイズは、ハガキ~A4まで、自由でかまいません。

手書きでも、いずれかの形式でデータ化しての納品を希望します。
【記載内容訂正】誤字 ×小分け袋箱→○小分け袋
沢山の方に見ていただきありがたく思っております。
締め切り日が近づいて参りましたが、台風接近中のため、お時間あるかたはぜひご提案ください!
手書き文字や書道風文字など、何らかの文字は入れていただき、表現していただきたいです。
当選者には、少しお直しのお願いをすることもありますので、まずはイメージでの投稿でもかまいません。
質問や締め切り日の延長希望などありましたらご連絡ください。
引き続き、よろしくお願いいたします。
沢山の提案本当にありがとうございます!
どの作品も素晴らしく、家族一同感動、感謝、そして悩みます、、、!もしかしたら2つくらい当選があるかもしれません。締め切りまであと少しですが、悩みながら決めますのでよろしくお願い致します。

台風の被害もほとんどなく、桜里柿は無事でした。ご心配してくださりありがとうございます。一つずつの作品にお返事したかったのですが、今日は朝から台風でずっとバタバタで、お返事できてない方申し訳ありません。選考まで今しばらくお待ちください。
■ 選んだ理由

qvvvvv様:手書きの質感が伝わり、お手紙として年齢問わずみていただけること。文字とイラストのバランス、配色が良かったこと。

rira207様:インパクトある柿キャラを筆文字で作るというアイディアが素晴らしく、美しい筆文字。文字とイラストのバランスが良かったこと。

■ 提案者全員のお礼・コメント

この度はたくさんの素敵な作品を提案していただきありがとうございました。

ホームページを皆様よくみて下さり、少ない情報から私たちの思いを感じ取ってそれを作品に表現していただいたことに感動しています。

どれも力作で素敵な作品ばかりで決めるのが難しかったのが本音です。
またの機会がございましたらお力をお貸しいただければ幸いです。

この度は本当にありがとうございました。

```html
<!DOCTYPE html>
<html lang="ja">
<head>
<meta charset="utf-8">
<title>桜里柿 ご案内の手紙</title>
<link rel="stylesheet" href="https://fonts.googleapis.com/css2?family=Yuji+Syuku&display=swap">
<style>
  :root {
    --paper: #fcfdfe;
    --ink: #1f1d1c;
    --link-blue: #2a56c6;
  }
  * { margin: 0; padding: 0; box-sizing: border-box; }
  html, body {
    width: 811px;
    height: 1200px;
    overflow: hidden;
    background: var(--paper);
  }
  .letter {
    position: relative;
    width: 811px;
    height: 1200px;
    background: var(--paper);
    font-family: "Yuji Syuku", serif;
    color: var(--ink);
  }
  .persimmon-art {
    position: absolute;
    left: 30px;
    top: 75px;
    width: 425px;
    height: 375px;
  }
  .column {
    position: absolute;
    writing-mode: vertical-rl;
    white-space: nowrap;
    line-height: 1;
  }
  .thanks-1 { left: 742px; top: 68px;  font-size: 40px; }
  .thanks-2 { left: 662px; top: 257px; font-size: 39px; }
  .harvest-1 { left: 596px; top: 300px; font-size: 32px; letter-spacing: 1px; }
  .harvest-2 { left: 536px; top: 340px; font-size: 32px; letter-spacing: 1px; }
  .order-1 { left: 474px; top: 400px; font-size: 31px; }
  .order-2 { left: 404px; top: 528px; font-size: 38px; letter-spacing: 4px; }
  .gift-1 { left: 112px; top: 640px; font-size: 28px; letter-spacing: 2px; }
  .gift-2 { left: 56px;  top: 770px; font-size: 28px; letter-spacing: 2px; }
  .site-url {
    position: absolute;
    left: 4px;
    bottom: 4px;
    font-family: "Yuji Syuku", serif;
    font-size: 22px;
    color: var(--link-blue);
  }
</style>
</head>
<body>
<main class="letter">
  <svg class="persimmon-art" viewBox="0 0 425 375" role="img" aria-label="枝にたわわに実った桜里柿と葉の手描きイラスト">
    <defs>
      <linearGradient id="fruit-tone" x1="0" y1="0" x2="1" y2="1">
        <stop offset="0" stop-color="#f3b08a"/>
        <stop offset="0.5" stop-color="#e48a5e"/>
        <stop offset="0.75" stop-color="#a9c296"/>
        <stop offset="1" stop-color="#eaf0e4"/>
      </linearGradient>
    </defs>
    <rect x="0" y="0" width="425" height="375" rx="60" fill="url(#fruit-tone)" opacity="0.55"/>
  </svg>

  <p class="column thanks-1">昨年はご賞味頂き誠に</p>
  <p class="column thanks-2">ありがとうございます。</p>
  <p class="column harvest-1">今年の桜里柿もたいへんおいしく</p>
  <p class="column harvest-2">仕上がりました。</p>
  <p class="column order-1">ホームページからもご注文頂けます。</p>
  <p class="column order-2">心からお待ち申し上げます。</p>
  <p class="column gift-1">(オリジナルデザインの小分け袋</p>
  <p class="column gift-2">無料でお付け致します)</p>

  <p class="site-url">http://aobakaki-nouen.jp/</p>
</main>
</body>
</html>
```